International business needs a web page design

We need a web page design for a new service that our new "sub-company" of our existing company will offer. We are based in Denmark, and our new "sub-company" is called 'Velkari'. The service we offer is automated server configuration and In-Depth monitoring, and optional operations support. Our monitoring has a lot of graphs (like those seen here: https://velkari.example/ with either black or white background ) and the website needs to communicate a sense of Security/safety and that our customers can relax, because we have the full overview of their service and servers. The website should not be with black background.

We deliver low price, high quality and professional operations - which we can do, because we automate it and have people with 15+ years of experience doing so.

We have attached :
a file with our logo : velkari
a file showing the content of the frontage : frontpage
a file showing the content of the user page(for logged in users) : User page
a file showing the pop-up dialog "page" : CallToAction_route
a file showing the 3-steps for the frontpage : 3-step for frontpage

Target Market(s)

Chief Technological officers (CTO's) and Developers (small business, run by developers) - who needs professional IT operations.

Industry/Entity Type

Business

Coding

Coded - Design and coding required

Number of Pages Required

3 page

Requirements
Must have
• Frontpage :
• A lot of visualization(some with people too) rather than a lot of text
• A short, describing text on front page telling what people get
• 3 steps showing people how it works. (Could be presented in a video placed on top of a big front image or perhaps with all 3 steps/pictures shown at the same time or perhaps in a completely different way).
Nice to have
• A big front image(perhaps a person with a cellphone showing graphs and a "all okay" message) with a text and the 3-steps pictures/or video on top of it
• 3 boxes under the front image/top of the site showing what benefits people get from the service
Should not have
• Not a black/dark site

```html
<!DOCTYPE html>
<html lang="en">
<head>
<meta charset="utf-8">
<title>Velkari – Instant server setup &amp; In-depth monitoring</title>
<link rel="stylesheet" href="https://fonts.googleapis.com/css2?family=Open+Sans:wght@400;600;700&display=swap">
<style>
  :root {
    --brand-blue: #1a9bd7;
    --ink: #333333;
    --nav-grey: #6b6b6b;
    --white: #ffffff;
    --hero-light: #b3b3b5;
    --hero-dark: #8f8f93;
    --step-band: rgba(128, 128, 132, 0.78);
    --cta-dark: #2f2f2f;
    --card-bg: #eeeeee;
    --card-text: #666666;
    --footer-bg: #3a3a3a;
    --footer-text: #d6d6d6;
    --footer-icon: #a8a8a8;
  }
  * { box-sizing: border-box; margin: 0; padding: 0; }
  html, body { width: 1200px; height: 890px; overflow: hidden; }
  body {
    position: relative;
    font-family: "Open Sans", Arial, sans-serif;
    background: var(--white);
    color: var(--ink);
  }
  a { color: inherit; text-decoration: none; }

  /* Header */
  .site-header { position: absolute; left: 0; top: 0; width: 1200px; height: 101px; background: var(--white); }
  .brand { position: absolute; left: 110px; top: 25px; display: flex; align-items: center; gap: 10px; }
  .brand-mark { width: 54px; height: 54px; border-radius: 50%; background: var(--brand-blue); flex: none; }
  .brand-text { display: flex; flex-direction: column; }
  .brand-name { font-size: 31px; font-weight: 600; line-height: 34px; color: var(--ink); letter-spacing: -0.5px; }
  .brand-tagline { font-size: 9.5px; font-weight: 600; color: var(--ink); line-height: 12px; }
  .main-nav { position: absolute; top: 44px; left: 641px; display: flex; }
  .main-nav a { font-size: 13.5px; color: var(--nav-grey); text-transform: uppercase; margin-right: 41px; }
  .main-nav a:last-child { margin-right: 0; }
  .main-nav a.is-active { color: var(--brand-blue); }

  /* Hero */
  .hero { position: absolute; left: 0; top: 101px; width: 1200px; height: 462px; }
  .hero-photo {
    position: absolute; inset: 0;
    background: linear-gradient(90deg, #c9c9cb 0%, var(--hero-light) 35%, #a6a6a9 60%, var(--hero-dark) 100%);
  }
  .hero-arrow { position: absolute; top: 216px; width: 20px; height: 30px; }
  .hero-arrow.prev { left: 20px; }
  .hero-arrow.next { left: 1160px; }
  .hero-copy { position: absolute; left: 709px; top: 30px; width: 360px; color: var(--white); }
  .hero-title { font-size: 28.5px; font-weight: 700; line-height: 36px; }
  .hero-lead { margin-top: 6px; font-size: 14.5px; line-height: 22.5px; }

  .steps { position: absolute; left: 711px; top: 158px; width: 342px; list-style: none; }
  .step { display: flex; height: 63px; margin-bottom: 9px; background: var(--step-band); }
  .step-number {
    width: 55px; background: var(--white); color: var(--brand-blue);
    display: flex; flex-direction: column; align-items: center; justify-content: center;
  }
  .step-number small { font-size: 14px; line-height: 16px; }
  .step-number strong { font-size: 27px; font-weight: 600; line-height: 28px; }
  .step-icon { width: 72px; display: flex; align-items: center; justify-content: center; }
  .step-label { display: flex; align-items: center; font-size: 16.5px; font-weight: 600; color: var(--white); line-height: 21px; width: 130px; }
  .cta-button {
    position: absolute; left: 711px; top: 375px; width: 342px; height: 44px;
    background: var(--cta-dark); color: var(--white);
    display: flex; align-items: center; justify-content: center; gap: 9px;
    font-size: 14.5px;
  }

  /* Benefits */
  .benefits { position: absolute; left: 110px; top: 582px; display: flex; gap: 19px; }
  .benefit { width: 315px; height: 183px; background: var(--card-bg); padding: 22px 22px 0 22px; position: relative; }
  .benefit-title { display: flex; align-items: center; gap: 8px; color: var(--brand-blue); font-size: 18.5px; font-weight: 400; line-height: 21px; height: 28px; }
  .benefit-title svg { flex: none; }
  .benefit-title.two-line { margin-top: -12px; height: 42px; line-height: 20px; }
  .benefit-body { margin-top: 9px; font-size: 12px; line-height: 18.5px; color: var(--card-text); }
  .benefit-title.two-line + .benefit-body { margin-top: 7px; }
  .read-more { position: absolute; left: 22px; top: 144px; display: flex; align-items: center; gap: 6px; font-size: 12.5px; font-weight: 600; color: #222; }

  /* Footer */
  .site-footer { position: absolute; left: 0; top: 787px; width: 1200px; height: 103px; background: var(--footer-bg); color: var(--footer-text); }
  .footer-nav { position: absolute; left: 110px; top: 26px; font-size: 12.5px; }
  .footer-nav span { margin: 0 10px; }
  .copyright { position: absolute; left: 110px; top: 56px; font-size: 12.5px; word-spacing: 2px; }
  .social { position: absolute; left: 1026px; top: 38px; display: flex; gap: 20px; }
  .social a { width: 22px; height: 22px; border-radius: 50%; background: var(--footer-icon); display: block; }
</style>
</head>
<body>

<header class="site-header">
  <a class="brand" href="https://velkari.example/">
    <span class="brand-mark"></span>
    <span class="brand-text">
      <span class="brand-name">Velkari</span>
      <span class="brand-tagline">Instant server setup &amp; In-depth monitoring</span>
    </span>
  </a>
  <nav class="main-nav">
    <a class="is-active" href="#">Home</a>
    <a href="#">Services</a>
    <a href="#">About us</a>
    <a href="#">Contact us</a>
    <a href="#">Login</a>
  </nav>
</header>

<section class="hero">
  <div class="hero-photo" role="img" aria-label="Smiling businessman in a suit holding out a smartphone showing an all-okay tick"></div>

  <svg class="hero-arrow prev" viewBox="0 0 20 30" aria-hidden="true"><polyline points="16,3 4,15 16,27" fill="none" stroke="#444" stroke-width="3"/></svg>
  <svg class="hero-arrow next" viewBox="0 0 20 30" aria-hidden="true"><polyline points="4,3 16,15 4,27" fill="none" stroke="#444" stroke-width="3"/></svg>

  <div class="hero-copy">
    <h1 class="hero-title">Quisque mattis volutpat</h1>
    <p class="hero-lead">Suspendisse dictum vestibulum augue, eu volutpat augue pharetra vitae. Donec vel purus at est congue aliquet. Sed vel sollicitudin magna.</p>
  </div>

  <ol class="steps">
    <li class="step">
      <div class="step-number"><small>Step</small><strong>1</strong></div>
      <div class="step-icon">
        <svg width="38" height="42" viewBox="0 0 38 42" aria-hidden="true">
          <circle cx="19" cy="11" r="10" fill="#fff"/>
          <path d="M2 42 V33 Q2 23 12 22 Q19 26 26 22 Q36 23 36 33 V42 Z" fill="#fff"/>
        </svg>
      </div>
      <div class="step-label">Choose Profile Image</div>
    </li>
    <li class="step">
      <div class="step-number"><small>Step</small><strong>2</strong></div>
      <div class="step-icon">
        <svg width="46" height="42" viewBox="0 0 46 42" aria-hidden="true">
          <g fill="#fff">
            <circle cx="16" cy="24" r="11"/>
            <rect x="13" y="9" width="6" height="30" rx="1"/>
            <rect x="1" y="21" width="30" height="6" rx="1"/>
            <rect x="13" y="9" width="6" height="30" rx="1" transform="rotate(45 16 24)"/>
            <rect x="13" y="9" width="6" height="30" rx="1" transform="rotate(-45 16 24)"/>
            <circle cx="36" cy="10" r="6"/>
            <rect x="34" y="1" width="4" height="18"/>
            <rect x="27" y="8" width="18" height="4"/>
            <circle cx="36" cy="34" r="5"/>
            <rect x="34.5" y="26" width="3" height="16"/>
            <rect x="28" y="32.5" width="16" height="3"/>
          </g>
          <circle cx="16" cy="24" r="4" fill="#8e8e91"/>
          <circle cx="36" cy="10" r="2.2" fill="#8e8e91"/>
          <circle cx="36" cy="34" r="1.8" fill="#8e8e91"/>
        </svg>
      </div>
      <div class="step-label">Run Command</div>
    </li>
    <li class="step">
      <div class="step-number"><small>Step</small><strong>3</strong></div>
      <div class="step-icon">
        <svg width="40" height="40" viewBox="0 0 40 40" aria-hidden="true">
          <rect x="1" y="18" width="9" height="20" rx="1.5" fill="#fff"/>
          <path d="M13 19 L20 8 Q21 2 25 3 Q28 5 26 12 L25 16 H35 Q39 17 38 21 Q37 24 36 25 Q38 28 35 30 Q36 33 33 34 Q34 38 29 38 H16 Q13 38 13 35 Z" fill="#fff"/>
        </svg>
      </div>
      <div class="step-label">Ready to Use</div>
    </li>
  </ol>

  <a class="cta-button" href="#">Click to get : Instant Server Setup Now
    <svg width="16" height="16" viewBox="0 0 16 16" aria-hidden="true"><circle cx="8" cy="8" r="6.8" fill="none" stroke="#fff" stroke-width="1.8"/><path d="M4.5 8 H11 M8 5 L11 8 L8 11" fill="none" stroke="#fff" stroke-width="1.8"/></svg>
  </a>
</section>

<section class="benefits">
  <article class="benefit">
    <h2 class="benefit-title"><svg width="18" height="18" viewBox="0 0 18 18" aria-hidden="true"><circle cx="9" cy="9" r="9" fill="#1a9bd7"/><path d="M4.5 9.2 L7.7 12.2 L13.5 6" fill="none" stroke="#fff" stroke-width="2.2"/></svg>It’s Fast and Easy</h2>
    <p class="benefit-body">Proin in luctus nibh, vitae fringilla ex. Duis id fermentum diam. Pellentesque sollicitudin felis dolor, eget mollis eros viverra ac. Suspendisse ut tellus sollicitudin.</p>
    <a class="read-more" href="#">READ MORE <svg width="12" height="12" viewBox="0 0 16 16" aria-hidden="true"><circle cx="8" cy="8" r="6.8" fill="none" stroke="#222" stroke-width="2"/><path d="M4.5 8 H11 M8 5 L11 8 L8 11" fill="none" stroke="#222" stroke-width="2"/></svg></a>
  </article>
  <article class="benefit">
    <h2 class="benefit-title"><svg width="18" height="18" viewBox="0 0 18 18" aria-hidden="true"><circle cx="9" cy="9" r="9" fill="#1a9bd7"/><path d="M4.5 9.2 L7.7 12.2 L13.5 6" fill="none" stroke="#fff" stroke-width="2.2"/></svg>Relax and Rest Assured</h2>
    <p class="benefit-body">Proin in luctus nibh, vitae fringilla ex. Duis id fermentum diam. Pellentesque sollicitudin felis dolor, eget mollis eros viverra ac. Suspendisse ut tellus sollicitudin.</p>
    <a class="read-more" href="#">READ MORE <svg width="12" height="12" viewBox="0 0 16 16" aria-hidden="true"><circle cx="8" cy="8" r="6.8" fill="none" stroke="#222" stroke-width="2"/><path d="M4.5 8 H11 M8 5 L11 8 L8 11" fill="none" stroke="#222" stroke-width="2"/></svg></a>
  </article>
  <article class="benefit">
    <h2 class="benefit-title two-line"><svg width="18" height="18" viewBox="0 0 18 18" aria-hidden="true"><circle cx="9" cy="9" r="9" fill="#1a9bd7"/><path d="M4.5 9.2 L7.7 12.2 L13.5 6" fill="none" stroke="#fff" stroke-width="2.2"/></svg><span>You’ll love your detailed Performance Graphs</span></h2>
    <p class="benefit-body">Proin in luctus nibh, vitae fringilla ex. Duis id fermentum diam. Pellentesque sollicitudin felis dolor, eget mollis eros viverra ac. Suspendisse ut tellus sollicitudin.</p>
    <a class="read-more" href="#">READ MORE <svg width="12" height="12" viewBox="0 0 16 16" aria-hidden="true"><circle cx="8" cy="8" r="6.8" fill="none" stroke="#222" stroke-width="2"/><path d="M4.5 8 H11 M8 5 L11 8 L8 11" fill="none" stroke="#222" stroke-width="2"/></svg></a>
  </article>
</section>

<footer class="site-footer">
  <nav class="footer-nav">
    <a href="#">Home</a><span>|</span><a href="#">Services</a><span>|</span><a href="#">About us</a><span>|</span><a href="#">Contact us</a><span>|</span><a href="#">Login</a>
  </nav>
  <p class="copyright">Copyright © 2014 Velkari. All rights reserved.</p>
  <div class="social">
    <a href="#" aria-label="Social profile one"></a>
    <a href="#" aria-label="Social profile two"></a>
  </div>
</footer>

</body>
</html>
```